Business Card and Letterhead for Nurlo - modern real estate business

I need a double sided business card design for Nurlo. Please see business card brief here https://papers.trelvimo.net/sheet/q/7XrTbaLeZpMmQ2uWvd9HkCj4yNoEfsGi3lRtAz_pk/view?mode=shared

Please feel free to design the business cards however you feel best. I am happy to give some creative freedoms and then provide feedback from there.

Please then also create a letterhead to match the business card design

Colors

Designer to choose colors to be used in the design.

Requirements
Must have
• Must be a modern, elegant business card which looks very professional

```html
<!DOCTYPE html>
<html lang="en">
<head>
<meta charset="utf-8">
<title>Nurlo Business Card</title>
<link href="https://fonts.googleapis.com/css2?family=Raleway:wght@400;500;600&display=swap" rel="stylesheet">
<style>
  :root {
    --stage: #d9d9d9;
    --card: #050505;
    --red: #c8101a;
    --red-deep: #9e0b12;
    --white: #ffffff;
    --photo-a: #8fa6b8;
    --photo-b: #5a4a40;
  }
  * { margin: 0; padding: 0; box-sizing: border-box; }
  html, body {
    width: 1200px; height: 812px; overflow: hidden;
    background: var(--stage);
    font-family: "Raleway", sans-serif;
  }
  .stage {
    position: relative; width: 1200px; height: 812px;
    display: flex; justify-content: center; align-items: center; gap: 80px;
  }
  .card {
    position: relative; width: 340px; height: 580px;
    background: var(--card); color: var(--white);
    overflow: hidden;
    box-shadow: 0 12px 30px rgba(0,0,0,.25);
  }
  /* front */
  .brand {
    position: absolute; top: 210px; left: 0; right: 0;
    text-align: center;
    font-size: 46px; font-weight: 500; letter-spacing: 6px;
    color: var(--red);
  }
  .address {
    position: absolute; bottom: 70px; left: 0; right: 0;
    text-align: center; font-size: 15px; line-height: 1.55; letter-spacing: .5px;
  }
  .address svg { display: block; margin: 0 auto 10px; }
  /* back */
  .portrait {
    position: absolute; top: 46px; left: 50%; transform: translateX(-50%);
    width: 98px; height: 98px; border-radius: 50%;
    background: radial-gradient(circle at 50% 35%, var(--photo-a), var(--photo-b));
    border: 2px solid #2a2a2a;
  }
  .person {
    position: absolute; top: 172px; left: 0; right: 0; text-align: center;
  }
  .person-name { font-size: 30px; font-weight: 600; letter-spacing: .5px; }
  .person-role { margin-top: 4px; font-size: 14px; color: var(--red); letter-spacing: .3px; }
  .contacts {
    position: absolute; top: 300px; left: 70px;
    list-style: none; font-size: 15px; letter-spacing: .8px;
  }
  .contacts li { display: flex; align-items: center; gap: 16px; margin-bottom: 16px; }
  .web {
    position: absolute; top: 420px; left: 0; right: 0; text-align: center;
    font-size: 15px; letter-spacing: 1px;
  }
  .web svg { display: block; margin: 0 auto 14px; }
  .wave { position: absolute; bottom: 0; left: 0; }
</style>
</head>
<body>
<main class="stage">
  <section class="card card-front">
    <div class="brand">NURLO</div>
    <address class="address" style="font-style:normal">
      <svg width="14" height="20" viewBox="0 0 14 20" aria-hidden="true">
        <path d="M7 0C3.1 0 0 3.1 0 7c0 5 7 13 7 13s7-8 7-13c0-3.9-3.1-7-7-7z" fill="var(--red)"/>
        <circle cx="7" cy="7" r="2.6" fill="var(--card)"/>
      </svg>
      PO Box 1180<br>Elmvale NSW 2900
    </address>
  </section>

  <section class="card card-back">
    <div class="portrait" role="img" aria-label="Portrait photo of the agent"></div>
    <div class="person">
      <div class="person-name">Liam Carter</div>
      <div class="person-role">Licenced Real Estate Agent</div>
    </div>
    <ul class="contacts">
      <li>
        <svg width="16" height="16" viewBox="0 0 24 24" aria-hidden="true">
          <path fill="var(--red)" d="M6.6 10.8a15.1 15.1 0 0 0 6.6 6.6l2.2-2.2c.3-.3.7-.4 1-.2 1.1.4 2.3.6 3.6.6.6 0 1 .4 1 1V20c0 .6-.4 1-1 1A17 17 0 0 1 3 4c0-.6.4-1 1-1h3.5c.6 0 1 .4 1 1 0 1.3.2 2.5.6 3.6.1.3 0 .7-.2 1z"/>
        </svg>
        0400 555 132
      </li>
      <li>
        <svg width="16" height="14" viewBox="0 0 24 18" aria-hidden="true">
          <rect width="24" height="18" rx="2" fill="var(--red)"/>
          <path d="M2 3l10 7 10-7" stroke="var(--card)" stroke-width="2" fill="none"/>
        </svg>
        liam@nurlo.com
      </li>
    </ul>
    <div class="web">
      <svg width="18" height="18" viewBox="0 0 24 24" aria-hidden="true" fill="none" stroke="var(--red)" stroke-width="2">
        <circle cx="12" cy="12" r="10"/>
        <ellipse cx="12" cy="12" rx="4.5" ry="10"/>
        <path d="M2 12h20"/>
      </svg>
      www.nurlo.com
    </div>
    <svg class="wave" width="340" height="70" viewBox="0 0 340 70" aria-hidden="true">
      <path d="M0 22 C 90 0, 170 60, 340 44 L340 70 L0 70 Z" fill="var(--red)"/>
      <path d="M0 40 C 100 30, 190 70, 340 58 L340 70 L0 70 Z" fill="var(--red-deep)" opacity=".6"/>
    </svg>
  </section>
</main>
</body>
</html>
```